Corporate Powerpoint templates

I wish to have a standardized template for our manufacturing company. We manufacture baseball caps for major sport leagues and teams.
Our powerpoint should be clean, yet stylish.
We do a lot of presentations for technical trainings, KPI reports, quality assurance training.
We have factories in China, Bangladesh, and Mexico, so the look and feel must be internationally accepted.

Target Market(s)

Branded customers

Industry/Entity Type

Headwear Manufacturing

Font styles to use
Sans Serif

Colors
00AB8E
00BBA5
67D7C9
C6EFE9
E9F9F6

Requirements
Must have
• Spreadsheet slides, graphs, photographic reports
Nice to have
• Sporty, trendy, yet corporate feel.

```html
<!DOCTYPE html>
<html lang="en">
<head>
<meta charset="utf-8">
<title>Headwear Corporate Deck – Template Overview</title>
<link rel="stylesheet" href="https://fonts.googleapis.com/css2?family=Montserrat:ital,wght@0,600;0,700;0,800;0,900;1,800&family=Open+Sans:wght@300;400;600;700&display=swap">
<style>
:root{
  --teal:#00AB8E;
  --teal-bright:#00BBA5;
  --teal-soft:#67D7C9;
  --mint:#C6EFE9;
  --mist:#E9F9F6;
  --band:#38B0A1;
  --ink:#111;
  --grey:#7a7a7a;
  --line:#e3e3e3;
}
*{box-sizing:border-box;margin:0;padding:0}
html,body{width:904px;height:1200px;overflow:hidden;background:#fff}
.canvas{position:relative;width:904px;height:1200px;overflow:hidden;background:#fff;font-family:'Open Sans',sans-serif}
.top-band{position:absolute;left:0;top:0;width:904px;height:314px;background:var(--band)}

/* hero slide */
.hero{position:absolute;left:35px;top:36px;width:847px;height:477px;overflow:hidden;
  background:linear-gradient(90deg,#fff 0%,#f1fbf9 22%,#b9ebe3 52%,#5fcfbf 80%,#3cc0ad 100%);
  box-shadow:0 2px 8px rgba(0,0,0,.2)}
.hero > *{position:absolute}
.hero-frame{left:20px;top:380px;width:3px;height:75px;background:var(--teal-soft);opacity:.6}
.hero-frame-b{left:20px;top:455px;width:100px;height:3px;background:var(--teal-soft);opacity:.6}
.hero-corner{left:0;bottom:0;width:120px;height:20px;background:var(--teal);clip-path:polygon(0 0,80% 0,100% 100%,0 100%)}
.hero-ball{left:75px;top:95px;width:280px;height:280px;border-radius:50%;
  background:radial-gradient(circle at 38% 35%,#fff 0%,#f4f4f4 55%,#d9d9d9 80%,#c4c4c4 100%);
  box-shadow:inset -12px -12px 30px rgba(0,0,0,.08)}
.hero-reflect{left:100px;top:370px;width:240px;height:80px;border-radius:50%;
  background:radial-gradient(ellipse at center,rgba(255,255,255,.9),rgba(255,255,255,0) 70%)}
.hero-title{right:99px;top:116px;text-align:right;font:900 30px/34px 'Montserrat',sans-serif;color:var(--ink);letter-spacing:.5px}
.hero-rule-1{left:602px;top:201px;width:245px;height:5px;background:var(--teal);clip-path:polygon(0 0,100% 0,100% 100%,4% 100%)}
.hero-rule-2{left:632px;top:213px;width:215px;height:4px;background:#e8f6f3;clip-path:polygon(0 0,100% 0,100% 100%,3% 100%)}
.hero-sub{right:105px;top:254px;font:300 16.5px 'Open Sans',sans-serif;color:#1a1a1a}
.hero-social{top:334px;width:25px;height:25px;border:1.5px solid #fff;border-radius:2px}
.hero-stripes{left:722px;top:433px;width:90px;height:11px}
.hero-page{right:35px;top:452px;font:400 9px 'Open Sans',sans-serif;color:var(--teal-soft)}

/* thumbnails */
.s{position:absolute;width:158px;height:89px;background:#fff;overflow:hidden;box-shadow:0 1px 3px rgba(0,0,0,.22)}
.s > *{position:absolute}
.t{font:700 4.4px 'Montserrat',sans-serif;color:var(--ink);white-space:nowrap;padding-bottom:2px;border-bottom:.6px solid var(--teal)}
.t.plain{border-bottom:none}
.p{font:400 1.9px/2.6px 'Open Sans',sans-serif;color:var(--grey)}
.p.w{color:#fff}
.lab{font:700 2.3px 'Montserrat',sans-serif;color:var(--ink);white-space:nowrap}
.lab.teal{color:var(--teal)}
.lab.w{color:#fff}
.foot{left:0;bottom:2px;width:118px;height:1.6px;background:var(--teal)}
.foot-str{right:10px;bottom:1.5px;width:18px;height:3px}
.img-sky{background:linear-gradient(160deg,#6fa8d8,#a9c9e2 55%,#4f7a57)}
.img-dark{background:linear-gradient(135deg,#3c3c3c,#1d1d1d 60%,#5a4636)}
.img-field{background:linear-gradient(180deg,#9fc4e4 0%,#cfdde8 45%,#5e9b4f 60%,#3f7d3a 100%)}
.img-teal{background:linear-gradient(135deg,#8fded2,#2fb3a1)}
.img-ball{border-radius:50%;background:radial-gradient(circle at 38% 35%,#fff 0%,#f1f1f1 60%,#cfcfcf 100%)}
.avatar{border-radius:50%;background:linear-gradient(160deg,#d8d8d8,#9c9c9c)}
.card{background:#fff;box-shadow:0 .5px 1.5px rgba(0,0,0,.2)}
.num{border:.6px solid var(--teal);border-radius:50%;font:700 3px 'Montserrat',sans-serif;display:flex;align-items:center;justify-content:center;color:var(--ink)}
.bar{height:2.6px;border-radius:1.3px}
</style>
</head>
<body>
<div class="canvas">
  <div class="top-band"></div>

  <!-- Hero slide -->
  <section class="hero" aria-label="Cover slide">
    <div class="hero-frame"></div>
    <div class="hero-frame-b"></div>
    <div class="hero-corner"></div>
    <div class="hero-reflect"></div>
    <div class="hero-ball" role="img" aria-label="Photo of a baseball with red stitching"></div>
    <h1 class="hero-title">PRESENTATION<br>TITLE HERE</h1>
    <div class="hero-rule-1"></div>
    <div class="hero-rule-2"></div>
    <p class="hero-sub">Subtitle Goes Here</p>
    <div class="hero-social" style="left:634px" aria-label="Social link"></div>
    <div class="hero-social" style="left:670px" aria-label="Social link"></div>
    <div class="hero-social" style="left:706px" aria-label="Social link"></div>
    <svg class="hero-stripes" viewBox="0 0 90 11"><polygon points="4,0 10,0 6,11 0,11" fill="#67D7C9"/><polygon points="13,0 19,0 15,11 9,11" fill="#67D7C9"/><polygon points="22,0 28,0 24,11 18,11" fill="#67D7C9"/><polygon points="31,0 90,0 86,11 27,11" fill="#e9f9f6"/></svg>
    <span class="hero-page">3</span>
  </section>

  <!-- Row 1 -->
  <div class="s" style="left:26px;top:547px;background:linear-gradient(135deg,#fff,#f4f4f4)">
    <svg style="left:0;top:0" width="158" height="89"><polygon points="20,0 45,0 25,30 0,30" fill="#eee"/><polygon points="120,0 158,0 158,20 105,20" fill="#f0f0f0"/></svg>
    <div class="lab" style="left:52px;top:28px;font-size:5px;font-weight:800;text-align:center;line-height:5.5px">PRESENTATION<br>&nbsp;&nbsp;TITLE HERE</div>
    <div style="left:0;top:42px;width:150px;height:1.2px;background:var(--teal)"></div>
    <div class="p" style="left:62px;top:48px;font-size:2.4px;color:#333">Subtitle Goes Here</div>
    <div style="left:67px;top:62px;width:4px;height:4px;border:.5px solid var(--teal)"></div>
    <div style="left:73px;top:62px;width:4px;height:4px;border:.5px solid var(--teal)"></div>
    <div style="left:79px;top:62px;width:4px;height:4px;border:.5px solid var(--teal)"></div>
    <div class="foot" style="width:80px;left:78px;background:var(--teal-soft)"></div>
  </div>

  <div class="s" style="left:201px;top:547px;background:linear-gradient(90deg,#fff 25%,#9fe2d7 60%,#2fb8a5)">
    <div class="img-ball" style="left:15px;top:20px;width:48px;height:48px" role="img" aria-label="Baseball photo"></div>
    <div class="lab" style="right:16px;top:20px;font-size:5px;font-weight:800;text-align:right;line-height:5.5px">PRESENTATION<br>TITLE HERE</div>
    <div style="left:86px;top:33px;width:72px;height:1.2px;background:var(--teal)"></div>
    <div class="p" style="left:112px;top:48px;font-size:2.4px;color:#222">Subtitle Goes Here</div>
    <div style="left:118px;top:62px;width:4px;height:4px;border:.5px solid #fff"></div>
    <div style="left:124px;top:62px;width:4px;height:4px;border:.5px solid #fff"></div>
    <div style="left:130px;top:62px;width:4px;height:4px;border:.5px solid #fff"></div>
    <div style="left:0;bottom:0;width:40px;height:6px;background:var(--teal);clip-path:polygon(0 0,80% 0,100% 100%,0 100%)"></div>
    <div style="left:125px;bottom:3px;width:25px;height:2px;background:#fff"></div>
  </div>

  <div class="s" style="left:375px;top:547px;background:linear-gradient(90deg,#2fb8a5,#9fe2d7 45%,#fff 78%)">
    <div class="lab" style="left:14px;top:20px;font-size:5px;font-weight:800;line-height:5.5px">PRESENTATION<br>&nbsp;&nbsp;TITLE HERE</div>
    <div style="left:0;top:33px;width:72px;height:1.2px;background:var(--teal)"></div>
    <div class="p" style="left:14px;top:48px;font-size:2.4px;color:#222">Subtitle Goes Here</div>
    <div style="left:14px;top:62px;width:4px;height:4px;border:.5px solid #fff"></div>
    <div style="left:20px;top:62px;width:4px;height:4px;border:.5px solid #fff"></div>
    <div style="left:26px;top:62px;width:4px;height:4px;border:.5px solid #fff"></div>
    <div class="img-ball" style="left:95px;top:20px;width:48px;height:48px" role="img" aria-label="Baseball photo"></div>
    <div class="p w" style="left:12px;bottom:3px">Copyright © 2024</div>
  </div>

  <div class="s" style="left:550px;top:547px">
    <div class="t" style="left:12px;top:14px">Presentation list</div>
    <div class="card" style="left:26px;top:25px;width:116px;height:58px"></div>
    <div style="left:30px;top:28px;width:108px;display:grid;grid-template-columns:38px 12px 46px 12px;row-gap:3px;font:600 1.9px 'Open Sans',sans-serif;color:#333">
      <span>Cover Slides</span><span style="color:var(--teal)">01</span><span>Section Slides</span><span style="color:var(--teal)">12</span>
      <span>About Us</span><span style="color:var(--teal)">02</span><span>Vision And Mission Slides</span><span style="color:var(--teal)">14</span>
      <span>Solution</span><span style="color:var(--teal)">04</span><span>Process Slides</span><span style="color:var(--teal)">16</span>
      <span>Who are we</span><span style="color:var(--teal)">06</span><span>Closing Slides</span><span style="color:var(--teal)">18</span>
      <span>Problem</span><span style="color:var(--teal)">08</span><span>Mockup Slides</span><span style="color:var(--teal)">19</span>
      <span>Event slide</span><span style="color:var(--teal)">10</span><span>Thankyou Slide</span><span style="color:var(--teal)">20</span>
    </div>
    <div class="foot"></div>
  </div>

  <div class="s" style="left:724px;top:547px">
    <div style="left:0;top:0;width:158px;height:26px;background:linear-gradient(180deg,#f6ece4,#fff)" role="img" aria-label="Photo of a baseball bat and ball"></div>
    <div class="avatar" style="left:64px;top:10px;width:28px;height:28px;border:1.5px solid #fff" role="img" aria-label="Founder portrait"></div>
    <div style="left:0;top:51px;width:36px;height:.8px;background:var(--teal)"></div>
    <div class="lab" style="left:38px;top:48px;font-size:4px;letter-spacing:.5px">FOUNDER</div>
    <div class="lab" style="left:90px;top:48px;font-size:4px;letter-spacing:.5px">MESSAGE'S</div>
    <div class="lab teal" style="left:68px;top:55px;font-size:2.2px">NORA VALE</div>
    <div class="p" style="left:24px;top:60px;width:112px;text-align:center">Lorem ipsum dolor sit amet, consectetur adipiscing elit. Maecenas porttitor congue massa. Fusce posuere, magna sed pulvinar ultricies, purus lectus malesuada libero, sit amet commodo magna eros quis urna.</div>
    <div class="foot"></div>
  </div>

  <!-- Row 2 -->
  <div class="s" style="left:26px;top:657px">
    <div class="t plain" style="left:68px;top:11px">About Us</div>
    <div class="p" style="left:18px;top:20px;width:122px;text-align:center">Lorem ipsum dolor sit amet, consectetur adipiscing elit. Maecenas porttitor congue massa. Fusce posuere, magna sed pulvinar ultricies, purus lectus malesuada libero, sit amet commodo magna eros quis urna. Nunc viverra imperdiet enim.</div>
    <div class="num" style="left:44px;top:49px;width:6px;height:6px"></div>
    <div class="num" style="left:76px;top:49px;width:6px;height:6px"></div>
    <div class="num" style="left:108px;top:49px;width:6px;height:6px"></div>
    <div class="lab" style="left:37px;top:60px;font-style:italic">Our Mission</div>
    <div class="lab" style="left:73px;top:60px;font-style:italic">History</div>
    <div class="lab" style="left:104px;top:60px;font-style:italic">Strategy</div>
    <div class="p" style="left:33px;top:65px;width:26px;text-align:center">Lorem ipsum dolor sit amet elit.</div>
    <div class="p" style="left:66px;top:65px;width:26px;text-align:center">Lorem ipsum dolor sit amet elit.</div>
    <div class="p" style="left:98px;top:65px;width:26px;text-align:center">Lorem ipsum dolor sit amet elit.</div>
    <div class="foot"></div>
  </div>

  <div class="s" style="left:201px;top:657px">
    <div class="img-dark" style="left:11px;top:13px;width:46px;height:58px" role="img" aria-label="Photo of a baseball in a glove"></div>
    <div class="t plain" style="left:64px;top:17px">Who We Are</div>
    <div class="p" style="left:64px;top:25px;width:86px">Lorem ipsum dolor sit amet, consectetur adipiscing elit. Maecenas porttitor congue massa. Fusce posuere, magna sed pulvinar ultricies, purus lectus malesuada libero, sit amet commodo magna eros quis urna. Nunc viverra imperdiet enim. Fusce est.</div>
    <div class="card" style="left:64px;top:62px;width:20px;height:11px"></div>
    <div style="left:86px;top:62px;width:20px;height:11px;background:var(--teal)"></div>
    <div class="card" style="left:108px;top:62px;width:20px;height:11px"></div>
    <div class="lab teal" style="left:70px;top:65px">150</div>
    <div class="lab w" style="left:92px;top:65px">215</div>
    <div class="lab" style="left:114px;top:65px">300+</div>
    <div class="foot"></div>
  </div>

  <div class="s" style="left:375px;top:657px">
    <div class="t" style="left:12px;top:11px">What We Offer</div>
    <div class="p" style="left:22px;top:20px;width:116px;text-align:center">Lorem ipsum dolor sit amet, consectetur adipiscing elit. Maecenas porttitor congue massa. Fusce posuere, magna sed pulvinar.</div>
    <div class="img-field" style="left:16px;top:32px;width:40px;height:23px" role="img" aria-label="Photo of a pitcher"></div>
    <div class="img-dark" style="left:60px;top:32px;width:40px;height:23px" role="img" aria-label="Photo of a batter"></div>
    <div class="img-sky" style="left:104px;top:32px;width:40px;height:23px" role="img" aria-label="Photo of a stadium game"></div>
    <div style="left:16px;top:57px;width:40px;height:17px;background:var(--teal)"></div>
    <div class="card" style="left:60px;top:57px;width:40px;height:17px"></div>
    <div style="left:104px;top:57px;width:40px;height:17px;background:var(--teal)"></div>
    <div class="lab w" style="left:23px;top:59px">Insert Your Text</div>
    <div class="lab teal" style="left:67px;top:59px">Insert Your Text</div>
    <div class="lab w" style="left:111px;top:59px">Insert Your Text</div>
    <div class="p w" style="left:19px;top:63px;width:34px;text-align:center">Lorem ipsum dolor sit amet, adipiscing elit.</div>
    <div class="p" style="left:63px;top:63px;width:34px;text-align:center">Lorem ipsum dolor sit amet, adipiscing elit.</div>
    <div class="p w" style="left:107px;top:63px;width:34px;text-align:center">Lorem ipsum dolor sit amet, adipiscing elit.</div>
    <div class="foot"></div>
  </div>

  <div class="s" style="left:550px;top:657px">
    <div style="left:0;top:0;width:52px;height:89px;background:var(--teal)"></div>
    <div class="lab w" style="left:12px;top:7px">Insert Your Text</div>
    <div class="p w" style="left:5px;top:12px;width:42px;text-align:center">Lorem ipsum dolor sit amet, adipiscing elit.</div>
    <div class="lab w" style="left:12px;top:34px">Insert Your Text</div>
    <div class="p w" style="left:5px;top:39px;width:42px;text-align:center">Lorem ipsum dolor sit amet, adipiscing elit.</div>
    <div class="lab w" style="left:12px;top:61px">Insert Your Text</div>
    <div class="p w" style="left:5px;top:66px;width:42px;text-align:center">Lorem ipsum dolor sit amet, adipiscing elit.</div>
    <div class="img-sky" style="left:52px;top:0;width:51px;height:84px" role="img" aria-label="Photo of a player catching a ball"></div>
    <div class="t plain" style="left:108px;top:16px">What We Offer</div>
    <div class="p" style="left:108px;top:24px;width:44px">Lorem ipsum dolor sit amet, consectetur adipiscing elit. Maecenas porttitor congue massa. Fusce posuere, magna sed pulvinar ultricies, purus lectus malesuada libero, sit amet commodo magna eros quis urna.</div>
    <div class="foot"></div>
  </div>

  <div class="s" style="left:724px;top:657px">
    <div class="lab" style="left:-4px;top:42px;font-size:3.6px;transform:rotate(-90deg);text-align:center;line-height:4px">Text Paragraph With<br>Two Options</div>
    <div class="p" style="left:44px;top:14px;width:104px">Lorem ipsum dolor sit amet, consectetur adipiscing elit. Maecenas porttitor congue massa. Fusce posuere, magna sed pulvinar ultricies, purus lectus malesuada libero, sit amet commodo magna eros quis urna. Nunc viverra imperdiet enim.</div>
    <div style="left:44px;top:47px;width:104px;height:.4px;background:var(--line)"></div>
    <div class="num" style="left:44px;top:44px;width:6px;height:6px">01</div>
    <div class="num" style="left:95px;top:44px;width:6px;height:6px">02</div>
    <div class="lab teal" style="left:44px;top:55px;font-style:italic">Lorem Ipsum Dolor Sit</div>
    <div class="lab teal" style="left:95px;top:55px;font-style:italic">Lorem Ipsum Dolor Sit</div>
    <div class="p" style="left:44px;top:60px;width:40px">Lorem ipsum dolor sit amet, consectetur adipiscing elit congue.</div>
    <div class="p" style="left:95px;top:60px;width:40px">Lorem ipsum dolor sit amet, consectetur adipiscing elit congue.</div>
    <div class="foot"></div>
  </div>

  <!-- Row 3 -->
  <div class="s" style="left:26px;top:766px">
    <div class="t plain" style="left:10px;top:10px">Text With Bullet Point</div>
    <div class="img-dark" style="left:9px;top:21px;width:52px;height:59px" role="img" aria-label="Photo of a baseball player"></div>
    <div style="left:61px;top:21px;width:36px;height:59px;background:var(--teal)"></div>
    <div style="left:66px;top:25px;width:9px;height:9px;border-radius:50%;background:#fff"></div>
    <div class="p w" style="left:66px;top:37px;width:28px;font-weight:600">Lorem ipsum dolor sit amet, consectetur adipiscing elit. Maecenas porttitor congue massa. Fusce posuere.</div>
    <div class="p" style="left:101px;top:24px;width:50px">• Lorem ipsum dolor sit amet.<br>• Maecenas porttitor congue massa.<br>• Purus lectus malesuada libero.<br>• Lorem ipsum dolor sit amet.<br>• Consectetur adipiscing elit.<br>• Lorem ipsum dolor sit amet.</div>
    <div class="foot"></div>
  </div>

  <div class="s" style="left:201px;top:766px">
    <div class="t" style="left:12px;top:11px">Our Advantages</div>
    <div style="left:15px;top:24px;width:130px;display:grid;grid-template-columns:1fr 1fr;row-gap:7px;column-gap:6px">
      <div style="position:relative;height:12px"><div class="num" style="position:absolute;left:0;top:0;width:9px;height:9px">01</div><div class="p" style="position:absolute;left:13px;top:0;width:46px"><b style="color:#222">Content Here</b><br>Lorem ipsum is simply dummy text.</div></div>
      <div style="position:relative;height:12px"><div class="num" style="position:absolute;left:0;top:0;width:9px;height:9px">04</div><div class="p" style="position:absolute;left:13px;top:0;width:46px"><b style="color:var(--teal)">Content Here</b><br>Lorem ipsum is simply dummy text.</div></div>
      <div style="position:relative;height:12px"><div class="num" style="position:absolute;left:0;top:0;width:9px;height:9px;color:var(--teal)">02</div><div class="p" style="position:absolute;left:13px;top:0;width:46px"><b style="color:var(--teal)">Content Here</b><br>Lorem ipsum is simply dummy text.</div></div>
      <div style="position:relative;height:12px"><div class="num" style="position:absolute;left:0;top:0;width:9px;height:9px">05</div><div class="p" style="position:absolute;left:13px;top:0;width:46px"><b style="color:#222">Content Here</b><br>Lorem ipsum is simply dummy text.</div></div>
      <div style="position:relative;height:12px"><div class="num" style="position:absolute;left:0;top:0;width:9px;height:9px">03</div><div class="p" style="position:absolute;left:13px;top:0;width:46px"><b style="color:#222">Content Here</b><br>Lorem ipsum is simply dummy text.</div></div>
      <div style="position:relative;height:12px"><div class="num" style="position:absolute;left:0;top:0;width:9px;height:9px">06</div><div class="p" style="position:absolute;left:13px;top:0;width:46px"><b style="color:var(--teal)">Content Here</b><br>Lorem ipsum is simply dummy text.</div></div>
    </div>
    <div class="foot"></div>
  </div>

  <div class="s" style="left:375px;top:766px">
    <div class="t" style="left:12px;top:11px">Partners Slide</div>
    <svg style="left:0;top:0" width="158" height="89">
      <g fill="#fff" stroke="#e6e6e6" stroke-width=".4">
        <rect x="28" y="22" width="18" height="14"/><rect x="58" y="22" width="18" height="14"/><rect x="88" y="22" width="18" height="14"/><rect x="118" y="22" width="18" height="14"/>
        <rect x="40" y="43" width="18" height="14"/><rect x="72" y="43" width="18" height="14"/><rect x="104" y="43" width="18" height="14"/>
        <rect x="28" y="64" width="18" height="14"/><rect x="58" y="64" width="18" height="14"/><rect x="88" y="64" width="18" height="14"/><rect x="118" y="64" width="18" height="14"/>
      </g>
      <g fill="#b8c7d6"><circle cx="37" cy="29" r="3"/><circle cx="97" cy="29" r="3"/><circle cx="49" cy="50" r="3"/><circle cx="67" cy="71" r="3"/></g>
      <g fill="#d9b98a"><rect x="64" y="26" width="6" height="6"/><rect x="78" y="47" width="6" height="6"/><rect x="34" y="68" width="6" height="6"/><rect x="94" y="68" width="6" height="6"/></g>
      <g fill="#7fa7c9"><rect x="121" y="27" width="12" height="4" rx="2"/><rect x="107" y="48" width="12" height="4" rx="2"/><rect x="121" y="69" width="12" height="4" rx="2"/></g>
    </svg>
    <div class="foot"></div>
  </div>

  <div class="s" style="left:550px;top:766px">
    <div class="t" style="left:12px;top:10px">Meet Our Experts</div>
    <div class="p" style="left:12px;top:20px;width:134px">Lorem ipsum dolor sit amet, consectetur adipiscing elit nam consequat et ipsum accumsan facilisis ligula lorem, hendrerit nec libero aliquam.</div>
    <div class="card" style="left:10px;top:36px;width:31px;height:44px"></div>
    <div style="left:45px;top:36px;width:31px;height:44px;background:var(--teal)"></div>
    <div class="card" style="left:80px;top:36px;width:31px;height:44px"></div>
    <div class="card" style="left:115px;top:36px;width:31px;height:44px"></div>
    <div class="avatar" style="left:19px;top:41px;width:13px;height:13px" role="img" aria-label="Portrait"></div>
    <div class="avatar" style="left:54px;top:41px;width:13px;height:13px;border:.6px solid #fff" role="img" aria-label="Portrait"></div>
    <div class="avatar" style="left:89px;top:41px;width:13px;height:13px" role="img" aria-label="Portrait"></div>
    <div class="avatar" style="left:124px;top:41px;width:13px;height:13px" role="img" aria-label="Portrait"></div>
    <div class="lab" style="left:16px;top:58px">L.CARTER</div>
    <div class="lab w" style="left:53px;top:58px">M.OSEI</div>
    <div class="lab" style="left:82px;top:58px">P.LINDQVIST</div>
    <div class="lab" style="left:120px;top:58px">J.MORENO</div>
    <div class="p" style="left:12px;top:63px;width:27px;text-align:center"><span style="color:var(--teal)">Player</span><br>E: mail@team.com<br>P: +00 000 000</div>
    <div class="p w" style="left:47px;top:63px;width:27px;text-align:center">Player<br>E: mail@team.com<br>P: +00 000 000</div>
    <div class="p" style="left:82px;top:63px;width:27px;text-align:center"><span style="color:var(--teal)">Player</span><br>E: mail@team.com<br>P: +00 000 000</div>
    <div class="p" style="left:117px;top:63px;width:27px;text-align:center"><span style="color:var(--teal)">Player</span><br>E: mail@team.com<br>P: +00 000 000</div>
    <div class="foot"></div>
  </div>

  <div class="s" style="left:724px;top:766px">
    <div style="left:12px;top:10px;width:134px;display:grid;grid-template-columns:repeat(4,30px);column-gap:4px;row-gap:5px">
      <div class="card" style="position:relative;height:33px"><div class="avatar" style="position:absolute;left:10px;top:3px;width:10px;height:10px"></div><div class="lab" style="position:absolute;left:5px;top:15px">L.CARTER</div><div class="p" style="position:absolute;left:2px;top:19px;width:26px;text-align:center"><span style="color:var(--teal)">Player</span><br>mail@team.com</div></div>
      <div class="card" style="position:relative;height:33px"><div class="avatar" style="position:absolute;left:10px;top:3px;width:10px;height:10px"></div><div class="lab" style="position:absolute;left:5px;top:15px">L.CARTER</div><div class="p" style="position:absolute;left:2px;top:19px;width:26px;text-align:center"><span style="color:var(--teal)">Player</span><br>mail@team.com</div></div>
      <div class="card" style="position:relative;height:33px"><div class="avatar" style="position:absolute;left:10px;top:3px;width:10px;height:10px"></div><div class="lab" style="position:absolute;left:5px;top:15px">L.CARTER</div><div class="p" style="position:absolute;left:2px;top:19px;width:26px;text-align:center"><span style="color:var(--teal)">Player</span><br>mail@team.com</div></div>
      <div class="card" style="position:relative;height:33px"><div class="avatar" style="position:absolute;left:10px;top:3px;width:10px;height:10px"></div><div class="lab" style="position:absolute;left:5px;top:15px">L.CARTER</div><div class="p" style="position:absolute;left:2px;top:19px;width:26px;text-align:center"><span style="color:var(--teal)">Player</span><br>mail@team.com</div></div>
      <div class="card" style="position:relative;height:33px"><div class="avatar" style="position:absolute;left:10px;top:3px;width:10px;height:10px"></div><div class="lab" style="position:absolute;left:5px;top:15px">L.CARTER</div><div class="p" style="position:absolute;left:2px;top:19px;width:26px;text-align:center"><span style="color:var(--teal)">Player</span><br>mail@team.com</div></div>
      <div class="card" style="position:relative;height:33px"><div class="avatar" style="position:absolute;left:10px;top:3px;width:10px;height:10px"></div><div class="lab" style="position:absolute;left:5px;top:15px">L.CARTER</div><div class="p" style="position:absolute;left:2px;top:19px;width:26px;text-align:center"><span style="color:var(--teal)">Player</span><br>mail@team.com</div></div>
      <div class="card" style="position:relative;height:33px"><div class="avatar" style="position:absolute;left:10px;top:3px;width:10px;height:10px"></div><div class="lab" style="position:absolute;left:5px;top:15px">L.CARTER</div><div class="p" style="position:absolute;left:2px;top:19px;width:26px;text-align:center"><span style="color:var(--teal)">Player</span><br>mail@team.com</div></div>
      <div class="card" style="position:relative;height:33px"><div class="avatar" style="position:absolute;left:10px;top:3px;width:10px;height:10px"></div><div class="lab" style="position:absolute;left:5px;top:15px">L.CARTER</div><div class="p" style="position:absolute;left:2px;top:19px;width:26px;text-align:center"><span style="color:var(--teal)">Player</span><br>mail@team.com</div></div>
    </div>
    <div class="foot"></div>
  </div>

  <!-- Row 4 -->
  <div class="s" style="left:26px;top:874px">
    <div class="t" style="left:12px;top:11px">Comparative Bar Charts</div>
    <div class="avatar" style="left:52px;top:25px;width:12px;height:12px" role="img" aria-label="Portrait"></div>
    <div class="lab" style="left:74px;top:27px;font-size:7px;font-weight:900">VS</div>
    <div class="avatar" style="left:93px;top:25px;width:12px;height:12px" role="img" aria-label="Portrait"></div>
    <div class="lab teal" style="left:42px;top:25px">Name</div>
    <div class="lab teal" style="left:108px;top:25px">Name</div>
    <div class="p" style="left:8px;top:30px;width:40px;text-align:right">Lorem ipsum dolor sit amet.</div>
    <div class="p" style="left:108px;top:30px;width:40px">Lorem ipsum dolor sit amet.</div>
    <svg style="left:0;top:40px" width="158" height="44" font-family="Montserrat" font-size="2" font-weight="700">
      <rect x="42" y="1" width="25" height="3" rx="1.5" fill="#00AB8E"/><text x="50" y="3.3" fill="#fff">40%</text><text x="72" y="3.3">Lorem Ipsum</text><rect x="92" y="1" width="48" height="3" rx="1.5" fill="#67D7C9"/><text x="130" y="3.3" fill="#fff">70%</text>
      <rect x="30" y="11" width="37" height="3" rx="1.5" fill="#00AB8E"/><text x="34" y="13.3" fill="#fff">60%</text><text x="72" y="13.3">Lorem Ipsum</text><rect x="92" y="11" width="26" height="3" rx="1.5" fill="#67D7C9"/><text x="100" y="13.3" fill="#fff">40%</text>
      <rect x="22" y="21" width="45" height="3" rx="1.5" fill="#00AB8E"/><text x="26" y="23.3" fill="#fff">70%</text><text x="72" y="23.3">Lorem Ipsum</text><rect x="92" y="21" width="20" height="3" rx="1.5" fill="#67D7C9"/><text x="98" y="23.3" fill="#fff">30%</text>
      <rect x="50" y="31" width="17" height="3" rx="1.5" fill="#00AB8E"/><text x="54" y="33.3" fill="#fff">20%</text><text x="72" y="33.3">Lorem Ipsum</text><rect x="92" y="31" width="48" height="3" rx="1.5" fill="#67D7C9"/><text x="130" y="33.3" fill="#fff">70%</text>
    </svg>
    <div class="foot"></div>
  </div>

  <div class="s" style="left:201px;top:874px">
    <div class="t" style="left:8px;top:9px">Giant Chart</div>
    <div class="lab" style="left:8px;top:20px">Seasons</div>
    <svg style="left:8px;top:25px" width="145" height="55" font-family="Open Sans" font-size="1.7" fill="#777">
      <rect x="0" y="0" width="112" height="46" fill="#f4f4f4"/>
      <g stroke="#e2e2e2" stroke-width=".3"><path d="M30 0V46M37 0V46M44 0V46M51 0V46M58 0V46M65 0V46M72 0V46M79 0V46M86 0V46M93 0V46M100 0V46M107 0V46"/><path d="M0 7H112M0 14H112M0 21H112M0 28H112M0 35H112"/></g>
      <text x="1" y="4">Holiday</text><text x="1" y="11">Summer Seasons</text><text x="1" y="18">Practice Free time</text><text x="1" y="25">Preseason</text><text x="1" y="32">Winter Seasons</text><text x="1" y="39">National team break</text>
      <rect x="37" y="2" width="14" height="3" fill="#67D7C9"/><rect x="30" y="9" width="18" height="3" fill="#67D7C9"/><rect x="44" y="16" width="7" height="3" fill="#67D7C9"/><rect x="51" y="23" width="12" height="3" fill="#67D7C9"/><rect x="79" y="30" width="16" height="3" fill="#67D7C9"/><rect x="93" y="37" width="17" height="3" fill="#67D7C9"/>
      <text x="30" y="50">May</text><text x="37" y="50">Jun</text><text x="44" y="50">Jul</text><text x="51" y="50">Aug</text><text x="58" y="50">Sep</text><text x="65" y="50">Oct</text><text x="72" y="50">Nov</text><text x="79" y="50">Dec</text><text x="86" y="50">Jan</text><text x="93" y="50">Feb</text><text x="100" y="50">Mar</text><text x="107" y="50">Apr</text>
      <g fill="#222" font-weight="700"><text x="116" y="3">Summer Seasons</text><text x="116" y="16">Preseason</text><text x="116" y="29">Winter Seasons</text><text x="116" y="42">Practice Free time</text></g>
      <text x="116" y="6">8 Weeks</text><text x="116" y="19">7 Weeks</text><text x="116" y="32">10 Weeks</text><text x="116" y="45">8 Weeks</text>
    </svg>
    <div class="foot"></div>
  </div>

  <div class="s" style="left:375px;top:874px">
    <div class="t" style="left:12px;top:11px">Event Schedule</div>
    <div class="p" style="left:12px;top:21px;width:126px">Lorem ipsum dolor sit amet, consectetur adipiscing elit. Maecenas porttitor congue massa. Fusce posuere, magna sed pulvinar ultricies.</div>
    <div class="p" style="left:20px;top:32px;color:#333">17 July 2023</div>
    <div class="p" style="left:63px;top:32px;color:#333">08 August 2023</div>
    <div class="p" style="left:106px;top:32px;color:#333">13 August 2023</div>
    <div class="lab" style="left:20px;top:38px">Our First Event</div>
    <div class="lab teal" style="left:63px;top:38px">Our Two Event</div>
    <div class="lab" style="left:106px;top:38px">Our Three Event</div>
    <div style="left:20px;top:46px;width:122px;height:.4px;background:#ccc"></div>
    <div style="left:21px;top:45px;width:2px;height:2px;border-radius:50%;background:#999"></div>
    <div style="left:64px;top:45px;width:2px;height:2px;border-radius:50%;background:var(--teal)"></div>
    <div style="left:107px;top:45px;width:2px;height:2px;border-radius:50%;background:#999"></div>
    <div class="img-sky" style="left:19px;top:50px;width:32px;height:27px" role="img" aria-label="Photo of a stadium"></div>
    <div class="img-field" style="left:62px;top:50px;width:32px;height:27px" role="img" aria-label="Photo of a ballpark"></div>
    <div class="img-field" style="left:105px;top:50px;width:32px;height:27px" role="img" aria-label="Photo of a ballpark at dusk"></div>
    <div class="foot"></div>
  </div>

  <div class="s" style="left:550px;top:874px">
    <div class="t" style="left:12px;top:11px">Event schedule</div>
    <div class="p" style="left:12px;top:21px;width:126px">Lorem ipsum dolor sit amet, consectetur adipiscing elit. Maecenas porttitor congue massa. Fusce posuere, magna sed pulvinar ultricies.</div>
    <div class="p" style="left:20px;top:31px;color:#333">03 September 2023</div>
    <div class="p" style="left:63px;top:31px;color:#333">22 October 2023</div>
    <div class="lab teal" style="left:20px;top:37px">Our Forth Event</div>
    <div class="lab" style="left:63px;top:37px">Our Fifth Event</div>
    <div style="left:20px;top:46px;width:75px;height:.4px;background:#ccc"></div>
    <div class="img-field" style="left:18px;top:50px;width:32px;height:27px" role="img" aria-label="Photo of a floodlit field"></div>
    <div class="img-sky" style="left:61px;top:50px;width:32px;height:27px" role="img" aria-label="Photo of a stadium"></div>
    <div class="card" style="left:103px;top:32px;width:40px;height:48px"></div>
    <div class="lab teal" style="left:106px;top:35px;width:34px;text-align:center;white-space:normal;font-style:italic">"Lorem ipsum dolor sit amet, consectetur adipiscing elit"</div>
    <div class="p" style="left:106px;top:49px;width:34px;text-align:center">Lorem ipsum dolor sit amet, consectetur adipiscing elit. Maecenas porttitor congue massa.</div>
    <div class="foot"></div>
  </div>

  <div class="s" style="left:724px;top:874px">
    <div class="t" style="left:12px;top:11px">Table Style</div>
    <svg style="left:12px;top:26px" width="134" height="52" font-family="Open Sans" font-size="1.8" fill="#555">
      <rect width="134" height="5" fill="#00BBA5"/>
      <g fill="#fff" font-weight="700"><text x="2" y="3.4">Name</text><text x="38" y="3.4">Number</text><text x="68" y="3.4">Profit Rate</text><text x="90" y="3.4">Option</text><text x="106" y="3.4">Rate</text><text x="118" y="3.4">Performance</text></g>
      <g stroke="#e6e6e6" stroke-width=".3"><path d="M0 12H134M0 19H134M0 26H134M0 33H134M0 40H134M0 47H134"/></g>
      <text x="2" y="10">Data One</text><text x="40" y="10">3,467</text><text x="72" y="10">20.45</text><text x="91" y="10">Yes</text><text x="107" y="10">79</text><text x="121" y="10">3,566</text>
      <text x="2" y="17">Data Two</text><text x="40" y="17">6,5444</text><text x="72" y="17">34.5</text><text x="91" y="17">Yes</text><text x="107" y="17">67</text><text x="121" y="17">3,997</text>
      <text x="2" y="24">Data Three</text><text x="40" y="24">54,333</text><text x="72" y="24">56.7</text><text x="91" y="24">No</text><text x="107" y="24">77</text><text x="121" y="24">9,887</text>
      <text x="2" y="31">Data Four</text><text x="40" y="31">7,655</text><text x="72" y="31">6.55</text><text x="91" y="31">No</text><text x="107" y="31">89</text><text x="121" y="31">97,666</text>
      <text x="2" y="38">Data Five</text><text x="40" y="38">7,665</text><text x="72" y="38">90</text><text x="91" y="38">Yes</text><text x="107" y="38">90</text><text x="121" y="38">98.9</text>
      <text x="2" y="45">Data Six</text><text x="40" y="45">9,999</text><text x="72" y="45">69</text><text x="91" y="45">No</text><text x="107" y="45">87</text><text x="121" y="45">98.7</text>
    </svg>
    <div class="foot"></div>
  </div>

  <!-- Row 5 -->
  <div class="s" style="left:26px;top:983px">
    <div style="left:80px;top:0;width:78px;height:89px;background:linear-gradient(160deg,#00AB8E,#67D7C9);clip-path:polygon(40% 0,100% 0,60% 100%,0 100%)"></div>
    <div style="left:66px;top:0;width:92px;height:89px;background:#fff;clip-path:polygon(85% 0,100% 0,100% 100%,55% 100%,57% 98%)"></div>
    <div class="t plain" style="left:12px;top:12px">Our Great Achievement</div>
    <div class="p" style="left:12px;top:20px;width:58px">Lorem ipsum dolor sit amet, consectetur adipiscing elit. Maecenas porttitor congue massa. Fusce posuere, magna sed pulvinar ultricies, purus lectus.</div>
    <div class="lab" style="left:18px;top:42px;font-style:italic">Description</div>
    <div class="p" style="left:18px;top:46px;width:50px">Lorem ipsum dolor sit amet, consectetur.</div>
    <div class="lab" style="left:18px;top:52px;font-style:italic">Description</div>
    <div class="p" style="left:18px;top:56px;width:50px">Lorem ipsum dolor sit amet, consectetur.</div>
    <div class="lab" style="left:18px;top:62px;font-style:italic">Description</div>
    <div class="p" style="left:18px;top:66px;width:50px">Lorem ipsum dolor sit amet, consectetur.</div>
    <div class="img-dark" style="left:92px;top:8px;width:27px;height:27px;border-radius:50%" role="img" aria-label="Photo of a trophy"></div>
    <div class="img-dark" style="left:115px;top:33px;width:27px;height:27px;border-radius:50%" role="img" aria-label="Photo of a trophy"></div>
    <div class="img-dark" style="left:90px;top:56px;width:27px;height:27px;border-radius:50%" role="img" aria-label="Photo of a trophy"></div>
    <div style="left:71px;top:14px;width:10px;height:10px;border-radius:50%;background:var(--teal);color:#fff;font:700 2.6px Montserrat,sans-serif;display:flex;align-items:center;justify-content:center">675</div>
    <div style="left:117px;top:71px;width:10px;height:10px;border-radius:50%;background:var(--teal);color:#fff;font:700 2.6px Montserrat,sans-serif;display:flex;align-items:center;justify-content:center">458</div>
    <div class="foot"></div>
  </div>

  <div class="s" style="left:201px;top:983px">
    <div class="t plain" style="left:8px;top:5px">Player Dashboard</div>
    <div class="p" style="left:126px;top:6px">Date Range: 2024</div>
    <div style="left:8px;top:13px;width:142px;height:23px;background:linear-gradient(90deg,#00BBA5,#9fe2d7)" role="img" aria-label="Banner with player portrait and baseball bat"></div>
    <div class="avatar" style="left:13px;top:15px;width:17px;height:19px;border-radius:2px"></div>
    <div class="p w" style="left:33px;top:17px;font-weight:600">Theo Brandt<br>Outfielder | Position<br>Team: League Team</div>
    <div class="p" style="left:14px;top:40px;color:#333"><b>Total Wins:</b> 42<br>Win Rate</div>
    <div class="p" style="left:50px;top:40px;color:#333"><b>Total Runs:</b> 210<br>Runs per Game</div>
    <div class="p" style="left:86px;top:40px;color:#333"><b>Total Hits:</b> 2,348<br>Home Runs</div>
    <div class="p" style="left:122px;top:40px;color:#333"><b>Stolen Bases:</b> 80<br>Caught Stealing</div>
    <div class="lab" style="left:10px;top:50px;font-size:1.9px">Activities Today</div>
    <div class="lab" style="left:100px;top:50px;font-size:1.9px">Player Batting</div>
    <svg style="left:10px;top:54px" width="90" height="28" font-family="Open Sans" font-size="1.6" fill="#999">
      <g stroke="#eee" stroke-width=".3"><path d="M6 2H60M6 9H60M6 16H60M6 23H60"/></g>
      <text x="0" y="3">600</text><text x="0" y="10">400</text><text x="0" y="17">200</text><text x="1" y="24">0</text>
      <rect x="20" y="18" width="3" height="5" fill="#67D7C9"/><rect x="28" y="13" width="3" height="10" fill="#00AB8E"/><rect x="36" y="5" width="3" height="18" fill="#111"/><rect x="44" y="10" width="3" height="13" fill="#67D7C9"/>
      <text x="26" y="27">Player Stats</text>
      <g font-size="1.5"><circle cx="64" cy="10" r=".8" fill="#00AB8E"/><text x="66" y="10.5">Total Singles</text><circle cx="64" cy="14" r=".8" fill="#67D7C9"/><text x="66" y="14.5">Total Doubles</text><circle cx="64" cy="18" r=".8" fill="#111"/><text x="66" y="18.5">Total Triples</text><circle cx="64" cy="22" r=".8" fill="#C6EFE9"/><text x="66" y="22.5">Total Homeruns</text></g>
    </svg>
    <svg style="left:100px;top:55px" width="50" height="26" font-family="Open Sans" font-size="1.5" fill="#999">
      <circle cx="11" cy="13" r="8" fill="none" stroke="#C6EFE9" stroke-width="2.5"/>
      <circle cx="11" cy="13" r="8" fill="none" stroke="#00BBA5" stroke-width="2.5" stroke-dasharray="34 50.3" transform="rotate(-90 11 13)"/>
      <circle cx="11" cy="13" r="8" fill="none" stroke="#111" stroke-width="2.5" stroke-dasharray="6 50.3" stroke-dashoffset="-34" transform="rotate(-90 11 13)"/>
      <circle cx="24" cy="7" r=".8" fill="#00BBA5"/><text x="26" y="7.5">Grounded</text><circle cx="24" cy="13" r=".8" fill="#111"/><text x="26" y="13.5">Sac Bunts</text><circle cx="24" cy="19" r=".8" fill="#C6EFE9"/><text x="26" y="19.5">Sac Flies</text>
    </svg>
    <div class="foot"></div>
  </div>

  <div class="s" style="left:375px;top:983px">
    <div class="t plain" style="left:8px;top:5px">Player Health Overview</div>
    <div class="p" style="left:126px;top:6px">Date Range: 2024</div>
    <div class="lab" style="left:8px;top:16px;font-size:1.9px">Health Curve</div>
    <svg style="left:8px;top:20px" width="58" height="30"><g stroke="#eee" stroke-width=".3"><path d="M4 4H58M4 11H58M4 18H58M4 25H58"/></g><path d="M6 24 C12 22,14 14,20 16 S28 20,32 12 S42 6,46 10 S54 4,58 3" fill="none" stroke="#67D7C9" stroke-width=".8"/></svg>
    <div class="lab" style="left:8px;top:53px;font-size:1.9px">Health Curve</div>
    <div class="lab teal" style="left:8px;top:63px;font-size:2.6px">Strength</div>
    <div class="p" style="left:8px;top:67px">Below normal</div>
    <svg style="left:32px;top:58px" width="34" height="14"><path d="M0 10 C6 4,10 12,16 7 S26 3,34 8" fill="none" stroke="#67D7C9" stroke-width=".7"/></svg>
    <div class="lab" style="left:68px;top:14px;font-size:1.9px">This Month Treatment Calendar</div>
    <svg style="left:68px;top:18px" width="84" height="14" font-family="Open Sans" font-size="2" fill="#555"><rect width="84" height="14" fill="#fafafa"/><text x="3" y="5" fill="#f39a6b">Sun</text><text x="15" y="5">Mon</text><text x="27" y="5">Tue</text><text x="39" y="5" fill="#00AB8E">Wed</text><text x="51" y="5">Thu</text><text x="63" y="5">Fri</text><text x="75" y="5">Sat</text><text x="3" y="11" fill="#f39a6b">02</text><text x="15" y="11">03</text><text x="27" y="11">04</text><text x="39" y="11" fill="#00AB8E">05</text><text x="51" y="11">06</text><text x="63" y="11">07</text><text x="75" y="11">08</text></svg>
    <div class="lab" style="left:68px;top:35px;font-size:1.9px">Player Appointment</div>
    <svg style="left:68px;top:39px" width="84" height="42" font-family="Open Sans" font-size="1.7" fill="#555">
      <g fill="#999"><text x="2" y="2">Name</text><text x="32" y="2">Speciality</text><text x="55" y="2">Date</text><text x="72" y="2">Time</text></g>
      <g stroke="#eee" stroke-width=".3"><path d="M0 4H84M0 17H84M0 30H84"/></g>
      <circle cx="4" cy="10" r="2.5" fill="#bbb"/><text x="9" y="10.5">Jay Reed</text><text x="32" y="10.5">Dentist</text><text x="55" y="10.5">27-5-2024</text><text x="72" y="10.5">11:00 PM</text>
      <circle cx="4" cy="23" r="2.5" fill="#bbb"/><text x="9" y="23.5">Eve Lane</text><text x="32" y="23.5">Psychologist</text><text x="55" y="23.5">15-6-2024</text><text x="72" y="23.5">10:00 AM</text>
      <circle cx="4" cy="36" r="2.5" fill="#bbb"/><text x="9" y="36.5">Ray Moss</text><text x="32" y="36.5">Therapist</text><text x="55" y="36.5">07-8-2024</text><text x="72" y="36.5">09:00 PM</text>
    </svg>
    <div class="foot"></div>
  </div>

  <div class="s" style="left:550px;top:983px">
    <div class="t" style="left:10px;top:11px">Player Dashboard</div>
    <div style="left:10px;top:22px;width:44px;height:60px;background:linear-gradient(180deg,#00AB8E,#67D7C9)"></div>
    <div class="avatar" style="left:19px;top:28px;width:25px;height:25px;border:1px solid #fff" role="img" aria-label="Player portrait"></div>
    <div class="lab w" style="left:21px;top:61px">KAI RENNER</div>
    <div class="p w" style="left:14px;top:65px;width:36px;text-align:center">Position: 2B<br>Team: Home Club<br>Age: 27</div>
    <div class="lab" style="left:60px;top:14px;font-size:1.9px">Market</div>
    <svg style="left:60px;top:18px" width="92" height="30" font-family="Open Sans" font-size="1.5" fill="#999"><g stroke="#eee" stroke-width=".3"><path d="M12 3H92M12 9H92M12 15H92M12 21H92"/></g><text x="0" y="4">25,000,000</text><text x="0" y="10">20,000,000</text><text x="0" y="16">15,000,000</text><text x="0" y="22">10,000,000</text><path d="M14 21 L22 19 L30 20 L38 16 L46 17 L54 12 L62 14 L70 9 L78 10 L88 5" fill="none" stroke="#00BBA5" stroke-width=".6"/><g fill="#00BBA5"><circle cx="22" cy="19" r=".6"/><circle cx="38" cy="16" r=".6"/><circle cx="54" cy="12" r=".6"/><circle cx="70" cy="9" r=".6"/><circle cx="88" cy="5" r=".6"/></g><text x="14" y="27">2010 2011 2012 2013 2014 2015 2016 2017 2018 2019 2020</text></svg>
    <div class="lab" style="left:60px;top:51px;font-size:1.9px">In Last Season</div>
    <div class="lab" style="left:106px;top:51px;font-size:1.9px">In Current Season</div>
    <svg style="left:60px;top:54px" width="92" height="28" font-family="Montserrat" font-size="2.4" font-weight="700">
      <path d="M16 18 A8 8 0 0 1 32 18" fill="none" stroke="#e6e6e6" stroke-width="1.6"/><path d="M16 18 A8 8 0 0 1 29 12" fill="none" stroke="#00AB8E" stroke-width="1.6"/><text x="21" y="18">30</text>
      <path d="M62 18 A8 8 0 0 1 78 18" fill="none" stroke="#e6e6e6" stroke-width="1.6"/><path d="M62 18 A8 8 0 0 1 76 13" fill="none" stroke="#00AB8E" stroke-width="1.6"/><text x="67" y="18">46</text>
      <circle cx="7" cy="24" r="2" fill="#ccc"/><circle cx="27" cy="24" r="2" fill="#ccc"/><circle cx="53" cy="24" r="2" fill="#ccc"/><circle cx="73" cy="24" r="2" fill="#ccc"/>
    </svg>
    <div class="foot"></div>
  </div>

  <div class="s" style="left:724px;top:983px">
    <div class="t" style="left:12px;top:11px">About Player</div>
    <div class="avatar" style="left:12px;top:24px;width:10px;height:10px" role="img" aria-label="Player portrait"></div>
    <div class="p" style="left:25px;top:26px;color:#222"><b>KAI RENNER</b><br>Home Club</div>
    <div class="p" style="left:60px;top:26px;color:#222"><b>Position</b><br>2B</div>
    <div class="p" style="left:74px;top:26px;color:#222"><b>Height</b><br>180 CM</div>
    <div class="p" style="left:88px;top:26px;color:#222"><b>Weight</b><br>82 KG</div>
    <div class="p" style="left:102px;top:26px;color:#222"><b>Age</b><br>27</div>
    <div class="p" style="left:113px;top:26px;color:#222"><b>Experience</b><br>10 Years</div>
    <div class="p" style="left:12px;top:37px;color:#222"><b>Performance</b></div>
    <div class="p" style="left:76px;top:37px;color:#222"><b>Player</b></div>
    <svg style="left:12px;top:42px" width="120" height="38" font-family="Open Sans" font-size="1.5" fill="#999">
      <path d="M6 32 L10 26 L14 28 L18 22 L22 27 L26 24 L30 18 L34 25 L38 20 L42 14 L46 22 L50 20 L54 18 L58 22 V32 Z" fill="#00BBA5"/>
      <path d="M70 32 L74 24 L78 28 L82 26 L86 18 L90 27 L94 22 L98 24 L102 14 L106 20 L110 22 L116 16 V32 Z" fill="#00BBA5"/>
      <path d="M5 2V32H60M69 2V32H118" fill="none" stroke="#ddd" stroke-width=".3"/>
      <text x="0" y="4">200</text><text x="0" y="12">150</text><text x="0" y="20">100</text><text x="0" y="28">50</text><text x="64" y="4">150</text><text x="64" y="16">100</text><text x="64" y="28">50</text>
    </svg>
    <div style="left:137px;top:24px;width:10px;height:10px;border-radius:50%;border:1px solid var(--teal-soft)"></div>
    <div style="left:137px;top:44px;width:10px;height:10px;border-radius:50%;border:1px solid #222"></div>
    <div style="left:137px;top:64px;width:10px;height:10px;border-radius:50%;border:1px solid var(--teal)"></div>
    <div class="p" style="left:137px;top:20px">Distance</div>
    <div class="p" style="left:135px;top:40px">Health Rate</div>
    <div class="p" style="left:135px;top:60px">Shot Speed</div>
    <div class="foot"></div>
  </div>

  <!-- Row 6 -->
  <div class="s" style="left:26px;top:1092px">
    <div class="t plain" style="left:8px;top:6px">Player Performance</div>
    <div class="lab" style="left:8px;top:14px;font-size:1.8px">Player Info</div>
    <div class="lab" style="left:54px;top:14px;font-size:1.8px">Appearances</div>
    <svg style="left:8px;top:17px" width="44" height="20" font-family="Open Sans" font-size="1.5" fill="#555"><rect width="44" height="3" fill="#00BBA5"/><text x="1" y="2.3" fill="#fff">player</text><text x="22" y="2.3" fill="#fff">Kai Renner</text><g stroke="#eee" stroke-width=".3"><path d="M0 7H44M0 11H44M0 15H44M0 19H44"/></g><text x="1" y="6">Age</text><text x="22" y="6">27</text><text x="1" y="10">Weight (KG)</text><text x="22" y="10">82</text><text x="1" y="14">Height (CM)</text><text x="22" y="14">180</text><text x="1" y="18">Position</text><text x="22" y="18">2B</text></svg>
    <div class="p" style="left:58px;top:20px;color:#00AB8E">Match Attendance<br><span style="color:#555">Appearances: 12</span></div>
    <div class="p" style="left:83px;top:20px;color:#00AB8E">Pass Accuracy<br><span style="color:#555">Passes: 196</span></div>
    <div class="p" style="left:106px;top:20px;color:#00AB8E">Goals<br><span style="color:#555">Assists: 13</span></div>
    <div class="p" style="left:128px;top:20px;color:#00AB8E">Shots on target<br><span style="color:#555">Shots: 68</span></div>
    <div class="lab" style="left:8px;top:40px;font-size:1.8px">Performance Analysis</div>
    <svg style="left:8px;top:44px" width="142" height="38" font-family="Open Sans" font-size="1.4" fill="#999">
      <path d="M6 2V30H42M52 2V30H90M100 2V30H140" fill="none" stroke="#ddd" stroke-width=".3"/>
      <g fill="#00BBA5"><circle cx="10" cy="24" r=".7"/><circle cx="12" cy="18" r=".7"/><circle cx="13" cy="22" r=".7"/><circle cx="15" cy="12" r=".7"/><circle cx="16" cy="20" r=".7"/><circle cx="20" cy="26" r=".7"/><circle cx="22" cy="16" r=".7"/><circle cx="30" cy="24" r=".7"/>
      <circle cx="58" cy="20" r=".7"/><circle cx="60" cy="14" r=".7"/><circle cx="64" cy="24" r=".7"/><circle cx="66" cy="10" r=".7"/><circle cx="70" cy="18" r=".7"/><circle cx="74" cy="22" r=".7"/><circle cx="78" cy="12" r=".7"/><circle cx="82" cy="26" r=".7"/>
      <circle cx="106" cy="16" r=".7"/><circle cx="110" cy="22" r=".7"/><circle cx="114" cy="12" r=".7"/><circle cx="118" cy="18" r=".7"/><circle cx="122" cy="24" r=".7"/><circle cx="126" cy="14" r=".7"/><circle cx="132" cy="20" r=".7"/></g>
      <text x="8" y="34">0%  50%  100%  150%</text><text x="54" y="34">0%  50%  100%  150%</text><text x="102" y="34">0%  50%  100%  150%</text>
      <text x="12" y="37">Successful Tackle Rate</text><text x="58" y="37">Successful Pass Rate</text><text x="104" y="37">Successful Shot Rate</text>
    </svg>
    <div class="foot"></div>
  </div>

  <div class="s" style="left:201px;top:1092px">
    <div class="t" style="left:12px;top:11px">Infographic Style</div>
    <svg style="left:55px;top:25px" width="50" height="50">
      <circle cx="25" cy="25" r="17" fill="none" stroke="#00BBA5" stroke-width="5" stroke-dasharray="14 4"/>
      <circle cx="25" cy="25" r="12" fill="#f3f3f3"/>
      <g fill="#fff"><circle cx="25" cy="8" r="2.5" stroke="#00AB8E" stroke-width=".5"/><circle cx="41" cy="20" r="2.5" stroke="#00AB8E" stroke-width=".5"/><circle cx="36" cy="39" r="2.5" stroke="#00AB8E" stroke-width=".5"/><circle cx="14" cy="39" r="2.5" stroke="#00AB8E" stroke-width=".5"/><circle cx="9" cy="20" r="2.5" stroke="#00AB8E" stroke-width=".5"/></g>
    </svg>
    <div class="p" style="left:20px;top:24px;width:36px;text-align:right">Step 01<br>Eros praesentium voluptas tempore alias.</div>
    <div class="p" style="left:10px;top:44px;width:44px;text-align:right">Step 02<br>Eros praesentium voluptas tempore alias.</div>
    <div class="p" style="left:20px;top:64px;width:36px;text-align:right">Step 03<br>Eros praesentium voluptas tempore alias.</div>
    <div class="p" style="left:104px;top:24px;width:40px">Step 04<br>Eros praesentium voluptas tempore alias.</div>
    <div class="p" style="left:108px;top:44px;width:42px">Step 05<br>Eros praesentium voluptas tempore alias.</div>
    <div class="p" style="left:104px;top:64px;width:40px">Step 06<br>Eros praesentium voluptas tempore alias.</div>
    <div class="foot"></div>
  </div>

  <div class="s" style="left:375px;top:1092px">
    <div style="left:8px;top:25px;width:60px;height:52px;background:linear-gradient(180deg,#2a2a2a,#5b6b78 60%,#c9c9c9)" role="img" aria-label="Laptop screen showing a racing photo"></div>
    <div class="t" style="left:105px;top:17px">Screen Mockup</div>
    <div class="p" style="left:82px;top:27px;width:66px;text-align:right">Lorem ipsum dolor sit amet, consectetur adipiscing elit. Maecenas porttitor congue massa. Fusce posuere, magna sed pulvinar ultricies, purus lectus malesuada libero, sit amet commodo magna eros quis urna. Nunc viverra imperdiet enim. Fusce est. Vivamus a tellus. Pellentesque habitant morbi tristique senectus et netus.</div>
    <div class="foot"></div>
  </div>

  <div class="s" style="left:550px;top:1092px;background:linear-gradient(90deg,#fff 35%,#8fdcd0 75%,#38b9a7)">
    <div class="img-ball" style="left:48px;top:8px;width:32px;height:32px" role="img" aria-label="Baseball photo"></div>
    <div class="lab" style="left:32px;top:50px;font-size:4.4px;font-weight:800">CONTACT US</div>
    <div style="left:0;top:57px;width:80px;height:.8px;background:var(--teal)"></div>
    <div style="left:22px;top:63px;width:5px;height:5px;border-radius:50%;background:var(--teal)"></div>
    <div class="p" style="left:30px;top:63px;width:40px"><b style="color:var(--teal)">Address</b><br>12 Sample Street, Sample City</div>
    <div style="left:82px;top:48px;width:5px;height:5px;border-radius:50%;background:var(--teal)"></div>
    <div class="card" style="left:90px;top:46px;width:52px;height:10px"></div>
    <div class="p" style="left:92px;top:47px;width:48px"><b style="color:var(--teal)">Email</b><br>hello@sample-mail.com</div>
    <div style="left:82px;top:63px;width:5px;height:5px;border-radius:50%;background:var(--teal)"></div>
    <div class="card" style="left:90px;top:61px;width:52px;height:10px"></div>
    <div class="p" style="left:92px;top:62px;width:48px"><b style="color:var(--teal)">Phone no</b><br>+00 000 000 0000</div>
    <div class="foot" style="background:var(--teal-bright)"></div>
  </div>

  <div class="s" style="left:724px;top:1092px;background:linear-gradient(135deg,#8fd9cd,#3fb3a3 60%,#2e8f83)" role="img" aria-label="Photo of a handshake over a city skyline">
    <div style="left:20px;top:62px;width:120px;height:17px;background:#fff"></div>
    <div class="img-ball" style="left:32px;top:62px;width:14px;height:14px" role="img" aria-label="Baseball photo"></div>
    <div class="lab" style="left:58px;top:66px;font-size:6px;font-weight:800;font-style:italic">THANKYOU</div>
    <div class="foot" style="background:var(--teal-soft)"></div>
  </div>

</div>
</body>
</html>
```